Web Design Project - Quillmore Analytics

I am a Mechanical Engineer running a one person consulting firm at this point. The hope is to expand in the future, but for now I simply need a website that conveys a professional appearance, and allows potential and existing clients to find me. Website design displaying contact information, CV for download, capabilities, past projects, etc. I've included four examples below from companies that provided the same service. I've only provided these as general reference for the type of work I do and how others have chosen to display this information. The design is completely at your discretion.

I've included the current Logo in the uploaded files section. I will provide content as requried.

http://www.torvanmech.com/
http://www.halberic.com/
http://www.rumblaxsystems.com/
http://dorwickmotive.net/

Industry/Entity Type

Consulting

```html
<!DOCTYPE html>
<html lang="en">
<head>
<meta charset="utf-8">
<title>Quillmore Analytics — Engineering Consultants</title>
<link href="https://fonts.googleapis.com/css2?family=Exo+2:ital,wght@0,700;1,700;1,800;1,900&family=Montserrat:wght@500;600&display=swap" rel="stylesheet">
<style>
:root{
  --orange:#f58220;
  --ink:#555353;
  --dark:#2b2b2b;
  --charcoal:#222222;
  --panel:#2f2c2c;
  --rule-gray:#6d6d6d;
  --white:#ffffff;
  --blue:#1a8fd0;
  --border:#cfcfcf;
}
*{margin:0;padding:0;box-sizing:border-box}
html,body{width:1200px;height:781px;overflow:hidden;background:var(--white)}
body{position:relative;font-family:"Exo 2",sans-serif}
.abs{position:absolute}
.top-rule{left:0;top:0;width:1200px;height:4px;background:var(--rule-gray)}
.top-rule span{display:block;width:606px;height:4px;background:var(--orange)}
.site-header{left:0;top:4px;width:1200px;height:54px;background:var(--white)}
.brand{left:222px;top:15px;display:flex;align-items:center;gap:7px;font-weight:700;font-size:14px;color:var(--orange);white-space:nowrap}
.brand i{width:10px;height:10px;background:var(--orange);display:block}
.nav a{position:absolute;top:20px;font-weight:800;font-style:italic;font-size:14px;color:var(--dark);text-decoration:none;letter-spacing:.3px}
.hero{left:0;top:58px;width:736px;height:112px;background:linear-gradient(120deg,#1c1c1c 0%,#6e6e6e 30%,#2a2a2a 50%,#9a9a9a 70%,#222 100%)}
.side-top{left:736px;top:58px;width:464px;height:283px;background:var(--charcoal)}
.side-panel{left:736px;top:341px;width:464px;height:440px;background:var(--panel)}
.crumb{left:231px;top:185px;font-weight:800;font-style:italic;font-size:12.5px;color:var(--ink);letter-spacing:.2px}
.crumb em{color:var(--orange);font-style:italic}
.welcome{left:229px;top:200px;font-weight:900;font-style:italic;font-size:48px;color:var(--ink);line-height:1}
.welcome-sub{left:234px;top:249px;font-weight:800;font-style:italic;font-size:13px;color:var(--ink)}
.option-title{top:306px;width:140px;text-align:center;font-weight:800;font-style:italic;font-size:13.5px;color:var(--dark);letter-spacing:.3px}
.option-photo{top:348px;width:136px;height:136px;border-radius:50%}
.btn{top:502px;height:26px;border:1px solid var(--border);border-radius:14px;display:flex;align-items:center;justify-content:center;gap:8px;font-family:"Montserrat",sans-serif;font-weight:600;font-size:9px;color:var(--blue);background:var(--white)}
.section-title{left:231px;top:576px;font-weight:800;font-style:italic;font-size:17px;color:var(--ink);line-height:.95}
.gear-badge{left:225px;top:622px;width:100px;height:100px;border-radius:50%;background:#5e5b5b}
.stat{top:623px;font-weight:800;font-style:italic;color:var(--ink)}
.stat small{display:block;font-size:11px;line-height:.95;height:23px}
.stat b{display:block;font-size:36px;color:var(--orange);font-weight:900;line-height:1;margin-top:-1px}
.testimonials{left:344px;top:682px;font-weight:900;font-style:italic;font-size:23px;color:var(--orange)}
.quote{right:503px;top:710px;width:380px;text-align:right;font-weight:800;font-style:italic;font-size:12px;line-height:19.2px;color:var(--orange)}
.side-heading{font-weight:900;font-style:italic;font-size:29px;color:var(--white);letter-spacing:.5px}
.what-copy{left:761px;top:406px;width:206px;font-weight:800;font-style:italic;font-size:12.5px;line-height:13.5px;color:var(--white)}
.side-art{left:764px;top:466px}
.specialties{list-style:none;left:768px;top:690px}
.specialties li{display:flex;align-items:center;gap:8px;height:19.2px;font-weight:800;font-style:italic;font-size:12px;color:var(--orange)}
.specialties li::before{content:"";width:0;height:0;border-top:8px solid #7a7676;border-left:8px solid transparent}
</style>
</head>
<body>
<div class="abs top-rule"><span></span></div>
<header class="abs site-header">
  <div class="abs brand"><i></i>Quillmore Analytics</div>
  <nav class="nav">
    <a href="#" style="left:394px">MENU</a>
    <a href="#" style="left:463px">MENU</a>
    <a href="#" style="left:533px">MENU</a>
    <a href="#" style="left:602px">MENU</a>
    <a href="#" style="left:672px">MENU</a>
    <a href="#" style="left:742px">MENU</a>
    <a href="#" style="left:824px">MENU</a>
  </nav>
</header>

<div class="abs hero" role="img" aria-label="Black and white 3D render of angular block shapes"></div>
<div class="abs side-top"></div>
<aside class="abs side-panel"></aside>

<p class="abs crumb"><em>ENGINEERING CONSULTANTS &gt;</em> QUILLMORE ANALYTICS</p>
<h1 class="abs welcome">Welcome</h1>
<p class="abs welcome-sub">to our website</p>

<h2 class="abs option-title" style="left:226px">OPTION 1</h2>
<h2 class="abs option-title" style="left:391px">OPTION 2</h2>
<h2 class="abs option-title" style="left:560px">OPTION 3</h2>

<div class="abs option-photo" style="left:222px;background:radial-gradient(circle at 40% 55%,#7fc3e8,#2a2f36 70%,#d8d8d8)" role="img" aria-label="Close-up photo of a precision measuring dial"></div>
<div class="abs option-photo" style="left:395px;background:radial-gradient(circle at 55% 45%,#2fa6f0,#0d47a6 60%,#111 100%)" role="img" aria-label="Photo of a blue machined rotary part"></div>
<div class="abs option-photo" style="left:562px;background:radial-gradient(circle at 60% 40%,#2a8ee8,#0b3f9a 60%,#dfe6ec 100%)" role="img" aria-label="Photo of blue gear teeth and a tool dial"></div>

<a class="abs btn" style="left:243px;width:94px">DETAILS
  <svg width="7" height="10" viewBox="0 0 7 10"><path d="M1 1l4 4-4 4" stroke="#1a8fd0" stroke-width="2" fill="none"/></svg></a>
<a class="abs btn" style="left:414px;width:94px">DETAILS
  <svg width="7" height="10" viewBox="0 0 7 10"><path d="M1 1l4 4-4 4" stroke="#1a8fd0" stroke-width="2" fill="none"/></svg></a>
<a class="abs btn" style="left:562px;width:134px">ROAD CONDITIONS</a>

<h2 class="abs section-title">WHAT QUILLMORE ANALYTICS<br>can do for you</h2>

<div class="abs gear-badge">
  <svg width="100" height="100" viewBox="0 0 100 100">
    <g transform="translate(42 58)" fill="#fff">
      <circle r="26"/>
      <rect x="-5" y="-34" width="10" height="12"/>
      <rect x="-5" y="-34" width="10" height="12" transform="rotate(45)"/>
      <rect x="-5" y="-34" width="10" height="12" transform="rotate(90)"/>
      <rect x="-5" y="-34" width="10" height="12" transform="rotate(135)"/>
      <rect x="-5" y="-34" width="10" height="12" transform="rotate(180)"/>
      <rect x="-5" y="-34" width="10" height="12" transform="rotate(225)"/>
      <rect x="-5" y="-34" width="10" height="12" transform="rotate(270)"/>
      <rect x="-5" y="-34" width="10" height="12" transform="rotate(315)"/>
      <circle r="4" fill="#5e5b5b"/>
    </g>
  </svg>
</div>

<div class="abs stat" style="left:343px"><small>years in the<br>business</small><b>24</b></div>
<div class="abs stat" style="left:422px"><small>misc.<br>statistic</small><b>3</b></div>
<div class="abs stat" style="left:479px"><small>misc.<br>statistic</small><b>82</b></div>
<div class="abs stat" style="left:554px"><small>misc.<br>statistic</small><b>4</b></div>

<h2 class="abs testimonials">Testimonials</h2>
<blockquote class="abs quote">I’ve been working with Quillmore Analytics steadily for over 6 years and I can tell you they outperform everytime.<br>- Dale Morrow, CEO/Founder Fernridge Grounds</blockquote>

<h2 class="abs side-heading" style="left:762px;top:363px">WHAT WE DO</h2>
<p class="abs what-copy">Bacon ipsum dolor sit amer shoulder biltong ball tip bacon spare ribs cow pig chicken.</p>
<svg class="abs side-art" width="120" height="120" viewBox="0 0 120 120" role="img" aria-label="Photo of a green circuit board with orange components">
  <defs><linearGradient id="boardTone" x1="0" y1="0" x2="1" y2="1"><stop offset="0" stop-color="#1f5a72"/><stop offset=".6" stop-color="#2d8c8a"/><stop offset="1" stop-color="#a0743a"/></linearGradient></defs>
  <polygon points="0,0 120,0 0,120" fill="url(#boardTone)"/>
</svg>

<h2 class="abs side-heading" style="left:764px;top:648px">SPECIALTIES</h2>
<ul class="abs specialties">
  <li>3-D Rendering</li>
  <li>City Consulting</li>
  <li>Parts and Forms</li>
  <li>Leveling</li>
</ul>
</body>
</html>
```